Copper Ridge Ag
Data Management Solutions
Thank You to all who entered, I liked all of them and therefore had a difficult time deciding, but had to pick one.
Thanks Again
well! nice greenery guys :)
Please check your private message.
Awaiting for your kind feedback
MegaMax
thanks,
InnovativeDesigner
Hello PH,
Please check draft #27 and a variation #25.
They can be modified upon request.
Thank you. Have a nice day.
please feel free to let me know the required changes so that your expectations are met.
hi ph
please check your private messege
Thanks.
please ceeck your private messege
I like #16, it is simple yet catchy and I really like the logo in the background. Keep them coming I will be chosing a winner tommorrow.
Thanks
I presented a draft #11. It can be modified upon request. Please download the draft for better quality. Thanks. Have a nice day.
I like the looks of number 3 the best, any other ideas along this route?
I have uploaded all the .ai files I have, hope this helps. Thanks
please post logos in ai.format they will be pixelated and look bad otherwise on the internet
two of your logos are wont open it says the link is damaged

```html
<!DOCTYPE html>
<html lang="en">
<head>
<meta charset="utf-8">
<title>Copper Ridge Ag — Data Management Solutions</title>
<link href="https://fonts.googleapis.com/css2?family=Arimo:ital,wght@0,400;0,700;1,400&family=Tinos:wght@400;700&display=swap" rel="stylesheet">
<style>
  :root{
    --sky-top:#dfe7ee;
    --sky-low:#f2ede0;
    --wheat-light:#e3b86a;
    --wheat:#c98f3c;
    --wheat-deep:#8d5a22;
    --brown-dark:#4a2a12;
    --brown-panel:rgba(74,44,20,.86);
    --brown-tab:#7a4a22;
    --brown-tab-light:#a87446;
    --nav-light:#f4ece0;
    --nav-mid:#e3d3bd;
    --nav-text:#5a3a1e;
    --ink:#3b2a1a;
    --cream:#f6ecd9;
    --red:#c4211c;
    --green:#4c7a22;
    --white:#ffffff;
  }
  *{box-sizing:border-box;margin:0;padding:0}
  html,body{width:1200px;height:881px;overflow:hidden}
  body{position:relative;font-family:"Arimo",Arial,sans-serif;color:var(--ink);background:var(--wheat)}
  .field-backdrop{position:absolute;inset:0;
    background:linear-gradient(180deg,var(--sky-top) 0%,var(--sky-low) 18%,var(--wheat-light) 30%,var(--wheat) 55%,var(--wheat-deep) 100%)}
  .abs{position:absolute}

  .follow{left:175px;top:28px;display:flex;align-items:center;gap:8px;font-weight:700;font-size:17px;color:var(--ink)}
  .social{display:flex;gap:8px;margin-left:8px}
  .social span{width:24px;height:24px;border-radius:4px;background:var(--brown-tab)}

  .brand{left:450px;top:20px;width:300px;text-align:center}
  .brand-dot{width:80px;height:80px;border-radius:50%;background:var(--green);margin:0 auto 10px}
  .brand-name{font-family:"Tinos",serif;font-weight:700;font-size:38px;color:var(--brown-dark);letter-spacing:.5px;line-height:1}
  .brand-tag{font-size:13px;color:var(--ink);margin-top:6px;border-top:1px solid var(--ink);display:inline-block;padding-top:3px}

  .call{left:752px;top:28px;font-weight:700;font-size:17px}
  .phone{left:888px;top:24px;display:flex;align-items:center;gap:6px;font-size:24px;color:var(--red)}
  .call-note{left:760px;top:58px;width:240px;font-size:10.5px;line-height:1.35;color:var(--ink)}

  .nav{left:180px;top:178px;width:840px;height:36px;border-radius:3px;
    background:linear-gradient(180deg,var(--nav-light),var(--nav-mid));display:flex;align-items:center;padding-left:8px;
    box-shadow:0 1px 3px rgba(0,0,0,.25)}
  .nav a{font-size:14px;color:var(--nav-text);text-decoration:none;padding:0 14px;height:26px;line-height:26px;border-right:1px solid #bfa98a}
  .nav a.current{background:#d8c5aa;border:1px solid #b89e7c}
  .search{margin-left:auto;margin-right:12px;width:110px;height:18px;border-radius:9px;background:var(--white);border:1px solid #bfa98a}

  .banner{left:180px;top:225px;width:840px;height:225px;
    background:linear-gradient(180deg,#7a5a36 0%,#c8923e 45%,#a96d26 75%,#6f4317 100%)}

  .services{left:180px;top:450px;width:840px;height:60px;display:flex}
  .service{flex:1;text-align:center;color:var(--white);
    background:linear-gradient(180deg,var(--brown-tab-light),var(--brown-tab));border-right:2px solid var(--brown-dark);padding-top:8px}
  .service:last-child{border-right:0}
  .service h3{font-weight:400;font-size:21px;line-height:1.1}
  .service p{font-size:13px;margin-top:3px}

  .content{left:180px;top:510px;width:840px;height:312px;background:var(--brown-panel);color:var(--cream);padding:16px 12px}
  .welcome{position:absolute;left:12px;top:16px;width:540px}
  .welcome h2,.testimonial h2{font-family:"Tinos",serif;font-weight:700;font-size:24px;color:var(--white);margin-bottom:8px}
  .welcome p{font-size:10.5px;line-height:1.45;margin-bottom:12px}
  .testimonial{position:absolute;left:580px;top:16px;width:250px}
  .testimonial h2{text-align:center}
  .testimonial blockquote{font-style:italic;font-size:12px;line-height:1.75;margin:10px 0 26px;padding-left:14px;position:relative}
  .testimonial blockquote::before{content:"\201C";position:absolute;left:0;top:-4px;font-size:20px;color:var(--white)}

  .footer{left:0;top:826px;width:1200px;height:55px;background:var(--brown-dark);text-align:center;color:var(--cream);font-size:11px;padding-top:10px}
  .footer nav a{color:var(--cream);text-decoration:none;margin:0 5px}
  .footer p{margin-top:10px}
</style>
</head>
<body>
  <div class="field-backdrop" role="img" aria-label="Photo of a golden wheat field under a pale cloudy sky"></div>

  <header>
    <div class="abs follow">Follow us
      <div class="social"><span></span><span></span><span></span><span></span></div>
    </div>

    <div class="abs brand">
      <div class="brand-dot"></div>
      <div class="brand-name">Copper Ridge Ag</div>
      <div class="brand-tag">Data Management Solutions</div>
    </div>

    <div class="abs call">Call us now</div>
    <div class="abs phone">
      <svg width="20" height="22" viewBox="0 0 20 22" aria-hidden="true"><path d="M4 1h4l1 5-3 2c1 3 3 6 6 8l2-3 5 1v4c0 2-2 3-4 3C7 21 0 13 1 5c0-2 1-4 3-4z" fill="var(--red)"/></svg>
      00-000-000
    </div>
    <p class="abs call-note">Aliquam erat volutpat. Aliquam tristique accumsan suscipit. Sed sollicitudin faucibus lorem eget commodo. Pellentesque accumsan tellus quis nibh vulputate non consequat neque vulputate. Morbi eleifend aliquam.</p>

    <nav class="abs nav">
      <a class="current" href="#">HOME</a>
      <a href="#">ABOUT US</a>
      <a href="#">SERVICES</a>
      <a href="#">CELIENT</a>
      <a href="#">SERVICES</a>
      <a href="#">CONTACT US</a>
      <span class="search"></span>
    </nav>
  </header>

  <div class="abs banner" role="img" aria-label="Photo of a combine harvester cutting ripe wheat"></div>

  <section class="abs services">
    <div class="service"><h3>SERVICE 1</h3><p>Lorum ipsum site doum</p></div>
    <div class="service"><h3>SERVICE 2</h3><p>Elam non diam nec nisl</p></div>
    <div class="service"><h3>SERVICE 3</h3><p>Vestibulum vel interdum</p></div>
    <div class="service"><h3>SERVICE 4</h3><p>Duis tincidunt justo nec augue</p></div>
  </section>

  <main class="abs content">
    <section class="welcome">
      <h2>Welcome to Copper Ridge Ag</h2>
      <p>Lorem ipsum dolor sit amet, consectetur adipiscing elit. Maecenas sapien diam, ultricies porttitor vestibulum quis, elementum id metus. Aliquam erat volutpat. Aliquam tristique accumsan suscipit. Sed sollicitudin faucibus lorem eget commodo. Pellentesque accumsan tellus quis nibh vulputate non consequat neque vulputate. Morbi eleifend aliquam consequat. Vestibulum mattis, lectus vitae ullamcorper commodo, lectus orci ultrices lacus, nec fringilla nulla neque a turpis. Quisque non mi justo, convallis tempus orci. Donec et nisi sapien, eu tempus massa. Fusce accumsan massa nec velit pellentesque ut pretium magna aliquet. Donec non porta lectus.</p>
      <p>Vestibulum accumsan diam metus, at aliquet metus. Vestibulum vel interdum ante. Donec tincidunt justo vitae enim aliquam tempus. Duis tincidunt justo nec augue posuere dapibus. Aenean vel justo orci. Suspendisse commodo, leo id aliquet faucibus, mauris nulla iaculis quam, eget consectetur quam mi ac purus. Suspendisse et urna et tellus euismod pretium. In neque tortor, tincidunt non fringilla consectetur, porttitor sodales ligula. Vivamus eleifend consectetur leo, ac hendrerit ipsum laoreet ut.</p>
    </section>
    <aside class="testimonial">
      <h2>Testimonial</h2>
      <blockquote>Ut commodo, nulla eu pellentesque mollis, ante condimentum turpis augue, eget faucibus dui magna ut ligula.</blockquote>
      <blockquote>Ut commodo, nulla eu pellentesque mollis, ante condimentum turpis augue, eget faucibus dui magna ut ligula.</blockquote>
    </aside>
  </main>

  <footer class="abs footer">
    <nav><a href="#">HOME</a> <a href="#">ABOUT US</a> <a href="#">SERVICES</a> <a href="#">CELIENT</a> <a href="#">SERVICES</a> <a href="#">CONTACT US</a></nav>
    <p>Copyright © 2011 Copper Ridge Ag , All Right Reseved</p>
  </footer>
</body>
</html>
```